data and media shredding company needs a flyer design

We need a flyer design for a startup company based on Long Island, NY. We shred all types of storage devices at the customers location. We want to emphasize on the dangers of identity theft and confidential information. With some focus on e-waste recycling. We want to coordinate the flyer with our website design.
www.vaultmincerservices.example

Target Market(s)

business owners that have personal information that needs to be destroyed

Font styles to use
Sans Serif

Colors

Designer to choose colors to be used in the design.

Requirements
Must have
• must have company name and logo, must have web address, must have phone number 855-310-4968, must have briefing of what we do, must be set for a trifold flyer

```html
<!DOCTYPE html>
<html lang="en">
<head>
<meta charset="utf-8">
<title>Vault Mincer Services – Trifold Flyer</title>
<link rel="stylesheet" href="https://fonts.googleapis.com/css2?family=Montserrat:wght@400;600;700;800&family=Open+Sans:wght@400;600&display=swap">
<style>
:root{
  --stage:#3a3a3c;
  --blue:#5b78b3;
  --blue-deep:#2d4a8c;
  --navy:#2f4260;
  --navy-dark:#1d2a40;
  --green:#7cc242;
  --grey:#b4b6ba;
  --white:#ffffff;
  --ink:#2a3550;
}
*{box-sizing:border-box;margin:0;padding:0}
html,body{width:1073px;height:1200px;overflow:hidden;background:var(--stage)}
body{position:relative;font-family:"Open Sans",Arial,sans-serif;color:var(--white)}
.sheet{position:absolute;left:56px;width:960px;height:540px;overflow:hidden;box-shadow:0 14px 30px rgba(0,0,0,.45)}
.sheet--outside{top:36px}
.sheet--inside{top:624px}
.sheet__art{position:absolute;inset:0}
.block{position:absolute}
.heading{font-family:"Montserrat",Arial,sans-serif;font-weight:800;text-transform:uppercase;letter-spacing:.5px}
.small{font-size:9px;line-height:1.45}
.green{color:var(--green)}
.center{text-align:center}

/* outside */
.secure{left:22px;top:78px;width:160px}
.secure__title{font-size:19px;color:var(--green);white-space:nowrap}
.secure__text{font-size:10.5px;line-height:1.3;margin-top:4px}
.secure__text b{display:block;font-size:9px;margin-top:3px}
.about{left:352px;top:36px;width:256px}
.about__title{font-size:18px;color:#c9d2e3;margin-bottom:12px}
.about__text{color:#b7c2d6;text-align:center;font-size:9.5px;line-height:1.5}
.accredit{left:420px;top:270px;width:120px;height:34px;border-radius:4px;background:var(--blue)}
.contact-icons{left:448px;top:318px;display:flex;gap:10px}
.copyright{left:340px;top:500px;width:280px;font-size:8.5px;color:#b7c2d6;text-align:center;line-height:1.5}
.brand{left:640px;top:0;width:320px;height:70px;display:flex;align-items:center;justify-content:center;gap:8px}
.brand__mark{width:22px;height:22px;border-radius:50%;background:var(--green)}
.brand__name{font-family:"Montserrat",Arial,sans-serif;font-weight:700;font-size:15px;color:var(--blue-deep)}
.keep{left:800px;top:140px;width:140px;text-align:right}
.keep__small{font-family:"Montserrat",Arial,sans-serif;font-weight:700;font-size:16px;line-height:1.05;text-transform:uppercase}
.keep__big{font-family:"Montserrat",Arial,sans-serif;font-weight:700;font-size:44px;line-height:1;color:var(--green)}
.tagline{left:670px;top:380px;width:270px;text-align:right}
.tagline__a{font-size:17px}
.tagline__b{font-size:17px;color:var(--green)}
.reach{left:670px;top:460px;width:270px;font-size:9.5px;line-height:1.8;text-align:right}
.reach svg{vertical-align:-2px;margin-right:4px}

/* inside */
.destruction{left:26px;top:34px;width:272px}
.destruction__title{font-size:17px;line-height:1.2;text-align:center;padding-bottom:6px;border-bottom:1px solid var(--green);margin-bottom:8px}
.destruction__text{color:#e3e9f4}
.destruction__text p+p{margin-top:8px}
.confidential{left:340px;top:30px;width:280px;text-align:center}
.confidential__a{font-family:"Montserrat",Arial,sans-serif;font-weight:400;font-size:20px;color:var(--green);text-transform:uppercase;line-height:1}
.confidential__b{font-family:"Montserrat",Arial,sans-serif;font-weight:800;font-size:22px;color:var(--blue-deep);text-transform:uppercase;border-bottom:1px solid var(--blue-deep);padding-bottom:4px}
.services{left:385px;top:110px}
.quote{left:660px;top:30px;width:280px;text-align:center}
.quote__title{font-size:14px}
.quote__sub{font-family:"Montserrat",Arial,sans-serif;font-weight:700;font-size:15px;color:var(--green);border-bottom:1px solid var(--green);padding-bottom:4px;margin:2px 30px 14px}
.quote__text{font-size:10px;line-height:1.45;font-weight:600;padding:0 24px}
.logo-box{left:705px;top:175px;width:190px;height:44px;background:var(--white);border-radius:3px;display:flex;align-items:center;justify-content:center;gap:7px}
.logo-box .brand__name{font-size:13px}
.logo-box .brand__mark{width:18px;height:18px}
.inside-icons{left:778px;top:238px}
</style>
</head>
<body>

<section class="sheet sheet--outside" aria-label="Outside of trifold flyer">
  <svg class="sheet__art" width="960" height="540" viewBox="0 0 960 540">
    <defs>
      <linearGradient id="driveDark" x1="0" y1="0" x2="1" y2="1">
        <stop offset="0" stop-color="#2a3954"/><stop offset=".5" stop-color="#6d7c93"/><stop offset="1" stop-color="#1a2436"/>
      </linearGradient>
      <linearGradient id="officeTone" x1="0" y1="0" x2="1" y2="1">
        <stop offset="0" stop-color="#6a6e74"/><stop offset=".6" stop-color="#3c3f46"/><stop offset="1" stop-color="#55483e"/>
      </linearGradient>
      <linearGradient id="drivesTone" x1="0" y1="0" x2="1" y2="1">
        <stop offset="0" stop-color="#e7e9ee"/><stop offset="1" stop-color="#9aa2ae"/>
      </linearGradient>
    </defs>
    <rect x="0" y="0" width="320" height="540" fill="var(--blue)"/>
    <rect x="320" y="0" width="320" height="540" fill="var(--navy)"/>
    <rect x="640" y="0" width="320" height="540" fill="var(--blue-deep)"/>
    <rect x="640" y="0" width="320" height="70" fill="var(--white)"/>
    <rect x="640" y="68" width="320" height="3" fill="var(--blue-deep)"/>
    <g role="img" aria-label="Photo of a businessman in glasses working at an office desk">
      <polygon points="640,71 960,71 960,230 640,400" fill="url(#officeTone)"/>
    </g>
    <g role="img" aria-label="Photo of a hard drive platter breaking into particles">
      <polygon points="0,330 640,395 640,540 0,540" fill="url(#driveDark)"/>
    </g>
    <g role="img" aria-label="Photo of stacked hard drives">
      <rect x="188" y="30" width="114" height="92" rx="10" fill="url(#drivesTone)" stroke="#ffffff" stroke-width="1.5"/>
    </g>
    <circle cx="210" cy="136" r="18" fill="#1f8f7a" stroke="#ffffff" stroke-width="3"/>
    <polygon points="0,300 640,372 640,382 0,312" fill="var(--white)"/>
    <polygon points="0,312 640,382 640,398 0,330" fill="var(--green)"/>
    <polygon points="640,390 960,210 960,240 640,415" fill="var(--green)"/>
    <polygon points="640,415 960,240 960,252 640,428" fill="var(--white)"/>
    <rect x="319" y="0" width="1" height="540" fill="rgba(0,0,0,.25)"/>
    <rect x="639" y="0" width="1" height="540" fill="rgba(0,0,0,.25)"/>
  </svg>

  <div class="block secure">
    <div class="heading secure__title">100% Secure</div>
    <p class="secure__text">Compliant Absolute Data Destruction On-Site<b>Any Where, Any Place, Any Time!</b></p>
  </div>

  <div class="block about">
    <h2 class="heading about__title center">About Us</h2>
    <p class="about__text">Vault Mincer Services was founded by Daniel Harlow, a longtime business owner who was born and raised on Long Island. Daniel has extensive hands-on experience in the data and equipment destruction industry. As a result, he saw the need for certified on-site destruction of data media, which is not only convenient for clients but also highly secure. Vault Mincer provides a unique data destruction service by not only picking up your data media but actually securely destroying the data and media on your site (home or office). This provides assurance to our clients that the data in a reusable form will never leave their site. We are primarily providing service to Nassau and Suffolk Counties, but are available to the Tri-State area.</p>
  </div>
  <div class="block accredit" role="img" aria-label="Accreditation badge"></div>
  <div class="block contact-icons" aria-label="Email">
    <svg width="16" height="12" viewBox="0 0 16 12"><rect x=".5" y=".5" width="15" height="11" fill="none" stroke="#c9d2e3"/><path d="M.5 .5 8 7l7.5-6.5" fill="none" stroke="#c9d2e3"/></svg>
  </div>
  <p class="block copyright">© Copyright 2019 Vault Mincer Services | All Rights Reserved |<br>Powered by Northgate Studio</p>

  <div class="block brand"><span class="brand__mark"></span><span class="brand__name">Vault Mincer Services</span></div>
  <div class="block keep">
    <div class="keep__small">Keep your<br>information</div>
    <div class="keep__big">SAFE</div>
  </div>
  <div class="block tagline">
    <div class="heading tagline__a">Data and Media</div>
    <div class="heading tagline__b">Shredding Company</div>
  </div>
  <div class="block reach">
    <div><svg width="11" height="9" viewBox="0 0 16 12"><rect x=".5" y=".5" width="15" height="11" fill="none" stroke="#fff"/><path d="M.5 .5 8 7l7.5-6.5" fill="none" stroke="#fff"/></svg>www.vaultmincerservices.example</div>
    <div><svg width="10" height="10" viewBox="0 0 12 12"><path d="M2 1h3l1 3-2 1a7 7 0 0 0 3 3l1-2 3 1v3c0 .6-.4 1-1 1A10 10 0 0 1 1 2c0-.6.4-1 1-1z" fill="#fff"/></svg>call toll free 855-310-4968</div>
  </div>
</section>

<section class="sheet sheet--inside" aria-label="Inside of trifold flyer">
  <svg class="sheet__art" width="960" height="540" viewBox="0 0 960 540">
    <defs>
      <linearGradient id="driveBlue" x1="0" y1="0" x2="1" y2="1">
        <stop offset="0" stop-color="#3b62a8"/><stop offset=".5" stop-color="#2f548f"/><stop offset="1" stop-color="#1e3a6a"/>
      </linearGradient>
      <linearGradient id="driveGreen" x1="0" y1="0" x2="1" y2="1">
        <stop offset="0" stop-color="#8fcf52"/><stop offset="1" stop-color="#4f8a2a"/>
      </linearGradient>
    </defs>
    <rect x="0" y="0" width="320" height="540" fill="var(--blue)"/>
    <rect x="320" y="0" width="320" height="540" fill="var(--grey)"/>
    <rect x="640" y="0" width="320" height="540" fill="var(--blue-deep)"/>
    <g role="img" aria-label="Blue-tinted photo of a hard drive breaking apart">
      <polygon points="0,344 640,320 640,540 0,540" fill="url(#driveBlue)"/>
    </g>
    <g role="img" aria-label="Green-tinted photo of an open hard drive">
      <polygon points="640,326 960,346 960,540 640,540" fill="url(#driveGreen)"/>
    </g>
    <polygon points="0,336 640,312 640,320 0,344" fill="var(--white)"/>
    <polygon points="640,314 960,336 960,346 640,326" fill="var(--white)"/>
    <rect x="319" y="0" width="1" height="540" fill="rgba(0,0,0,.2)"/>
    <rect x="639" y="0" width="1" height="540" fill="rgba(0,0,0,.2)"/>
  </svg>

  <div class="block destruction">
    <h2 class="heading destruction__title">Hard Drive &amp;<br>Media Destruction</h2>
    <div class="small destruction__text">
      <p>Erasing, degaussing, or formatting hard drives and media may leave them vulnerable for data theft as data may still remain on the drives. The only sure way to be certain that important data, confidential files, privacy information etc. are actually destroyed is to physically shred the drive/media. We provide a unique data destruction service by not only picking up your data media, but actually securely destroying the data and media on your site.</p>
      <p>The media is shredded onsite in our mobile shredder trailer. We document the actual destruction with photographs and videos which are provided to each client along with a certificate of destruction listing all serial numbers of the destroyed drives/media. This provides assurance to our clients that the data in a reusable form will never leave their site.</p>
    </div>
  </div>

  <div class="block confidential">
    <div class="confidential__a">Confidential</div>
    <div class="confidential__b">Information</div>
  </div>

  <svg class="block services" width="190" height="180" viewBox="0 0 190 180" aria-label="Service overview diagram">
    <circle cx="95" cy="88" r="82" fill="var(--blue-deep)" stroke="#ffffff" stroke-width="2"/>
    <circle cx="95" cy="88" r="86" fill="none" stroke="var(--green)" stroke-width="1"/>
    <path d="M95 6 A82 82 0 0 1 172 63 L95 88 Z" fill="#2c5ea8"/>
    <path d="M18 63 A82 82 0 0 1 95 6 L95 88 Z" fill="#235296"/>
    <circle cx="95" cy="88" r="30" fill="var(--blue-deep)" stroke="#ffffff" stroke-width="3"/>
    <line x1="95" y1="58" x2="95" y2="6" stroke="#ffffff" stroke-width="3"/>
    <line x1="66" y1="79" x2="18" y2="63" stroke="#ffffff" stroke-width="3"/>
    <line x1="124" y1="79" x2="172" y2="63" stroke="#ffffff" stroke-width="3"/>
    <rect x="40" y="36" width="20" height="16" rx="2" fill="#d6f0c0"/>
    <rect x="118" y="30" width="20" height="16" rx="2" fill="#d6f0c0"/>
    <text x="95" y="92" fill="#fff" font-family="Montserrat, sans-serif" font-weight="700" font-size="9" text-anchor="middle">SERVICE</text>
    <text x="46" y="62" fill="#fff" font-family="Open Sans, sans-serif" font-size="4.5" text-anchor="middle">PAPER &amp; FILE</text>
    <text x="46" y="68" fill="#fff" font-family="Open Sans, sans-serif" font-size="4.5" text-anchor="middle">SHREDDING</text>
    <text x="140" y="56" fill="#fff" font-family="Open Sans, sans-serif" font-size="4.5" text-anchor="middle">E-WASTE</text>
    <text x="140" y="62" fill="#fff" font-family="Open Sans, sans-serif" font-size="4.5" text-anchor="middle">RECYCLING</text>
    <text x="95" y="133" fill="#fff" font-family="Montserrat, sans-serif" font-weight="600" font-size="6.5" text-anchor="middle">HARD DRIVE</text>
    <text x="95" y="142" fill="#fff" font-family="Montserrat, sans-serif" font-weight="600" font-size="6.5" text-anchor="middle">&amp; MEDIA</text>
    <text x="95" y="151" fill="#fff" font-family="Montserrat, sans-serif" font-weight="600" font-size="6.5" text-anchor="middle">DESTRUCTION</text>
  </svg>

  <div class="block quote">
    <div class="heading quote__title">Destroy With Confidence</div>
    <div class="quote__sub">Get A Free Quote</div>
    <p class="quote__text">Our shredding service will destroy your hard drives or electronic media devices, rendering them useless for data recovery.</p>
  </div>
  <div class="block logo-box"><span class="brand__mark"></span><span class="brand__name">Vault Mincer Services</span></div>
  <div class="block inside-icons" aria-label="Email">
    <svg width="16" height="12" viewBox="0 0 16 12"><rect x=".5" y=".5" width="15" height="11" fill="none" stroke="#fff"/><path d="M.5 .5 8 7l7.5-6.5" fill="none" stroke="#fff"/></svg>
  </div>
</section>

</body>
</html>
```